Brookvale Homes Flyer

Quarter-page leave-behind flyer for a commercial cleaning company (print)

ABOUT US
Quillon Commercial Cleaning is a Texas-owned commercial cleaning company serving Austin for over 20 years. We were recently named to Brookvale Homes's Capital Partner Roster Circle, a preferred vendor program covering apartment communities across the Austin metro. Our sales team will hand this flyer to apartment community managers during property visits.

THE JOB THIS FLYER MUST DO
A busy property manager should scan it in five seconds, understand what we do, trust us and keep the card on their desk. The call to action is booking a free walkthrough of their community. Do not include any pricing.

SPECS
Size: 4.25 x 5.5 inches (quarter of a letter page), single sided, portrait. Print ready with 0.125 inch bleed, CMYK, 300 dpi minimum. Vector preferred.

REQUIRED CONTENT
Headline: The clean your residents notice.
Badge or tagline: Brookvale Homes's Approved Austin Cleaning Company.
Supporting line: Preferred Vendor Partner in BVH's Capital Partner Roster Circle. Texas-owned, serving Austin for 20+ years.
Services (icons welcome): recurring janitorial, floor strip wax and buff, carpet extraction, windows and glass, upholstery care, pressure washing, move-in and move-out cleans, damage restoration.
Trust points: licensed and insured, background-checked crews, TrudeLink compliant, invoicing through Supplier Nook and Halvex Systems.

Social proof line: Already trusted by BVH communities. Ask your peers at The Wendlow and The Fennick on Garrow.

Call to action: Book a free walkthrough of your community. Call or email 512-555-0147 or support@quillonclean-example.com

STYLE DIRECTION
Clean, crisp and premium. Whiteness and shine should feel like part of the message. We like a deep green and teal palette with one warm accent, but strong alternative directions are welcome. Custom icons over clip art.
AVOID
Stock photos of cleaners with buckets, cartoon mascots, sparkle overload, cluttered layouts, any prices or dollar amounts.
DELIVERABLES
Print-ready PDF with bleed and crop marks, plus editable source files (AI, PSD or Figma). A version with our logo placement marked, since we will supply the logo file to the winner.

```html
<!DOCTYPE html>
<html lang="en">
<head>
<meta charset="utf-8">
<title>Brookvale Homes Flyer – Quillon Commercial Cleaning</title>
<link href="https://fonts.googleapis.com/css2?family=Poppins:wght@400;500;600;700;800&display=swap" rel="stylesheet">
<style>
  :root{
    --forest:#0c4a33;
    --forest-deep:#083a28;
    --teal:#15978d;
    --teal-light:#2fb3a8;
    --ink:#0f3d2b;
    --mist:#e4e8e7;
    --paper:#ffffff;
    --canvas:#9a9a9c;
  }
  *{box-sizing:border-box;margin:0;padding:0}
  html,body{width:1200px;height:2400px;overflow:hidden;background:var(--canvas);font-family:'Poppins',sans-serif}
  .flyer-frame{position:absolute;left:30px;top:462px;width:1140px;height:1476px;box-shadow:0 6px 24px rgba(0,0,0,.25)}
  .flyer{position:absolute;left:0;top:0;width:950px;height:1230px;transform:scale(1.2);transform-origin:0 0;background:var(--paper);overflow:hidden;color:var(--ink)}
  .flyer-bg{position:absolute;left:0;top:0;width:950px;height:640px}
  .hero-photo{position:absolute;left:430px;top:0;width:520px;height:560px;background:linear-gradient(90deg,rgba(12,74,51,1) 0%,rgba(12,74,51,.55) 30%,rgba(120,170,155,.55) 60%,rgba(200,220,215,.7) 100%)}
  .brand{position:absolute;left:52px;top:48px;font-weight:700;font-size:46px;line-height:1;color:var(--teal);letter-spacing:-1px}
  .headline{position:absolute;left:52px;top:160px;font-weight:800;font-size:47px;line-height:57px;color:var(--paper);text-transform:uppercase;letter-spacing:.3px}
  .headline .accent{color:var(--teal-light)}
  .headline .light{font-weight:400}
  .approval-badge{position:absolute;left:52px;top:287px;width:460px;height:75px;background:var(--paper);padding:9px 0 0 30px;color:var(--forest);font-size:22px;line-height:29px;text-transform:uppercase}
  .approval-badge::before{content:"";position:absolute;left:-1px;top:0;width:0;height:0;border-top:37.5px solid transparent;border-bottom:37.5px solid transparent;border-left:12px solid var(--forest)}
  .approval-badge strong{font-weight:700;display:block}
  .supporting{position:absolute;left:52px;top:398px;font-size:16.5px;line-height:23px;color:var(--paper)}
  .supporting .years{font-weight:800;font-size:26px;color:var(--teal-light)}
  .section-heading{position:absolute;left:52px;top:622px;width:846px;height:42px}
  .section-heading::before{content:"";position:absolute;left:0;right:0;top:21px;height:1.5px;background:var(--teal)}
  .section-heading span{position:absolute;left:220px;top:0;width:508px;height:42px;border:1.5px solid var(--teal);border-radius:22px;background:var(--paper);text-align:center;font-weight:700;font-size:21px;line-height:39px;text-transform:uppercase;color:var(--ink)}
  .section-heading em{font-style:normal;color:var(--teal)}
  .services{position:absolute;left:52px;top:683px;width:846px;height:270px}
  .service{position:absolute;width:200px;text-align:center;font-size:16.5px;line-height:21px;color:var(--ink)}
  .service svg{display:block;margin:0 auto 6px;width:76px;height:76px}
  .service b{font-weight:700}
  .divider{position:absolute;top:0;width:1px;height:268px;background:var(--teal)}
  .divider::after{content:"";position:absolute;left:-3px;top:128px;width:7px;height:14px;background:var(--paper)}
  .trust-bar{position:absolute;left:52px;top:997px;width:846px;height:71px;background:var(--teal);border-radius:36px}
  .trust-item{position:absolute;top:-14px;text-align:center;color:var(--paper);font-weight:700;font-size:17px;line-height:21px}
  .trust-item .tick{display:block;margin:0 auto 4px;width:30px;height:30px}
  .social-proof{position:absolute;left:0;width:950px;top:1080px;text-align:center;font-size:16.5px;line-height:22px;color:var(--ink)}
  .social-proof strong{font-weight:700}
  .cta-band{position:absolute;left:0;top:1137px;width:950px;height:81px;background:var(--forest)}
  .cta-text{position:absolute;left:52px;top:16px;font-weight:700;font-size:16.5px;line-height:22px;color:var(--paper);text-align:right;width:245px}
  .cta-text em{font-style:normal;color:var(--teal-light)}
  .cta-phone{position:absolute;left:348px;top:24px;font-weight:700;font-size:22px;line-height:30px;color:var(--paper);display:flex;align-items:center;gap:9px}
  .cta-email{position:absolute;left:612px;top:26px;font-size:17px;line-height:26px;color:var(--paper);display:flex;align-items:center;gap:8px}
</style>
</head>
<body>
<div class="flyer-frame">
<main class="flyer">

  <svg class="flyer-bg" viewBox="0 0 950 640" aria-hidden="true">
    <rect width="950" height="640" fill="var(--forest)"/>
  </svg>
  <div class="hero-photo" role="img" aria-label="Photo of a uniformed cleaner squeegeeing a tall glass window in a bright lobby"></div>
  <svg class="flyer-bg" viewBox="0 0 950 640" aria-hidden="true">
    <path d="M0,480 C160,560 330,605 520,580 C700,555 830,470 950,460 L950,640 L0,640 Z" fill="var(--paper)"/>
    <path d="M420,600 C600,590 760,500 850,480 C900,470 935,480 950,495 L950,600 C900,520 820,520 720,560 C620,600 520,610 420,600 Z" fill="var(--mist)"/>
    <path d="M85,535 C300,625 560,610 760,510 C830,475 900,470 950,510 L950,530 C890,495 830,500 760,535 C560,630 300,640 85,535 Z" fill="var(--teal)"/>
  </svg>

  <div class="brand">quillon</div>

  <h1 class="headline">The <span class="accent">Clean</span> Your<br>Residents <span class="light">Notice</span></h1>

  <div class="approval-badge"><strong>Brookvale Homes's Approved</strong>Austin Cleaning Company.</div>

  <p class="supporting">Preferred Vendor Partner in BVH's Capital<br>Partner Roster Circle. Texas-owned,<br>serving Austin for <span class="years">20+ years.</span></p>

  <h2 class="section-heading"><span>Cleaning <em>Solutions</em> for Every Need</span></h2>

  <section class="services">
    <div class="divider" style="left:167px"></div>
    <div class="divider" style="left:410px"></div>
    <div class="divider" style="left:648px"></div>

    <div class="service" style="left:-38px;top:0">
      <svg viewBox="0 0 76 76"><circle cx="38" cy="38" r="36" fill="none" stroke="var(--teal)" stroke-width="2.5"/><path d="M20 48 h10 l10 5 l16 -8 M20 44 v10" fill="none" stroke="var(--teal)" stroke-width="3" stroke-linecap="round"/><path d="M30 24 l6 14 M46 24 l-6 14" stroke="var(--teal)" stroke-width="3" stroke-linecap="round"/><circle cx="38" cy="20" r="3" fill="var(--teal)"/></svg>
      <b>Recurring</b><br>Janitorial</div>
    <div class="service" style="left:185px;top:0">
      <svg viewBox="0 0 76 76"><circle cx="38" cy="38" r="36" fill="none" stroke="var(--teal)" stroke-width="2.5"/><path d="M22 50 h14 v-10 h-10 Z M40 50 h14 l-4 -10 h-10 Z M22 54 h14 v4 h-18 Z M40 54 h16 l2 4 h-18 Z" fill="var(--teal)"/><path d="M32 22 v8 M28 26 h8 M44 20 v8 M40 24 h8" stroke="var(--teal)" stroke-width="2.5"/></svg>
      <b>Floor Strip</b><br>Wax and Buff</div>
    <div class="service" style="left:428px;top:0">
      <svg viewBox="0 0 76 76"><circle cx="38" cy="38" r="36" fill="none" stroke="var(--teal)" stroke-width="2.5"/><rect x="22" y="22" width="10" height="32" rx="3" fill="none" stroke="var(--teal)" stroke-width="3"/><rect x="32" y="24" width="22" height="28" fill="none" stroke="var(--teal)" stroke-width="3"/><path d="M38 32 l9 6 l-9 6 Z" fill="var(--teal)"/></svg>
      <b>Carpet</b><br>Extraction</div>
    <div class="service" style="left:662px;top:0">
      <svg viewBox="0 0 76 76"><circle cx="38" cy="38" r="36" fill="none" stroke="var(--teal)" stroke-width="2.5"/><rect x="24" y="20" width="28" height="32" fill="none" stroke="var(--teal)" stroke-width="3"/><rect x="30" y="25" width="16" height="22" fill="var(--teal)"/><path d="M20 56 h36" stroke="var(--teal)" stroke-width="3"/></svg>
      <b>Windows &amp;<br>Glass</b> Cleaning</div>

    <div class="service" style="left:-38px;top:145px">
      <svg viewBox="0 0 76 76"><circle cx="38" cy="38" r="36" fill="none" stroke="var(--teal)" stroke-width="2.5"/><path d="M26 38 v-10 a6 6 0 0 1 6 -6 h12 a6 6 0 0 1 6 6 v10" fill="none" stroke="var(--teal)" stroke-width="3"/><rect x="20" y="36" width="36" height="10" rx="4" fill="none" stroke="var(--teal)" stroke-width="3"/><path d="M25 46 v8 M51 46 v8" stroke="var(--teal)" stroke-width="3"/></svg>
      <b>Upholstery</b><br>Care</div>
    <div class="service" style="left:185px;top:145px">
      <svg viewBox="0 0 76 76"><circle cx="38" cy="38" r="36" fill="none" stroke="var(--teal)" stroke-width="2.5"/><path d="M22 24 h18 v8 h-10 l-4 14 h-6 l3 -14 h-1 Z" fill="var(--teal)"/><rect x="34" y="38" width="18" height="18" rx="3" fill="none" stroke="var(--teal)" stroke-width="3"/><path d="M46 22 l8 -3 M46 27 h9 M46 32 l8 3" stroke="var(--teal)" stroke-width="2"/></svg>
      <b>Pressure</b><br>Washing</div>
    <div class="service" style="left:428px;top:145px">
      <svg viewBox="0 0 76 76"><circle cx="38" cy="38" r="36" fill="none" stroke="var(--teal)" stroke-width="2.5"/><path d="M50 18 v22" stroke="var(--teal)" stroke-width="3"/><path d="M42 40 h16 l-2 14 h-12 Z" fill="var(--teal)"/><path d="M24 44 h14 l-3 10 h-10 Z" fill="none" stroke="var(--teal)" stroke-width="3"/><path d="M28 24 v8 M24 28 h8 M38 30 v6 M35 33 h6" stroke="var(--teal)" stroke-width="2.5"/></svg>
      <b>Move-in &amp;<br>Move-out</b> cleans</div>
    <div class="service" style="left:662px;top:145px">
      <svg viewBox="0 0 76 76"><circle cx="38" cy="38" r="36" fill="none" stroke="var(--teal)" stroke-width="2.5"/><path d="M24 24 l28 28 M52 24 l-28 28" stroke="var(--teal)" stroke-width="5" stroke-linecap="round"/><circle cx="38" cy="38" r="7" fill="var(--paper)" stroke="var(--teal)" stroke-width="3"/></svg>
      <b>Damage</b><br>Restoration</div>
  </section>

  <section class="trust-bar">
    <div class="trust-item" style="left:22px;width:128px"><svg class="tick" viewBox="0 0 30 30"><rect x="2" y="2" width="26" height="26" rx="4" fill="var(--paper)" stroke="var(--teal)" stroke-width="2"/><path d="M8 15 l5 5 l9 -11" fill="none" stroke="var(--teal)" stroke-width="3"/></svg>Licensed<br>and Insured</div>
    <div class="trust-item" style="left:170px;width:218px"><svg class="tick" viewBox="0 0 30 30"><rect x="2" y="2" width="26" height="26" rx="4" fill="var(--paper)" stroke="var(--teal)" stroke-width="2"/><path d="M8 15 l5 5 l9 -11" fill="none" stroke="var(--teal)" stroke-width="3"/></svg>Background-checked<br>Crews</div>
    <div class="trust-item" style="left:410px;width:130px"><svg class="tick" viewBox="0 0 30 30"><rect x="2" y="2" width="26" height="26" rx="4" fill="var(--paper)" stroke="var(--teal)" stroke-width="2"/><path d="M8 15 l5 5 l9 -11" fill="none" stroke="var(--teal)" stroke-width="3"/></svg>TrudeLink<br>Compliant</div>
    <div class="trust-item" style="left:560px;width:272px"><svg class="tick" viewBox="0 0 30 30"><rect x="2" y="2" width="26" height="26" rx="4" fill="var(--paper)" stroke="var(--teal)" stroke-width="2"/><path d="M8 15 l5 5 l9 -11" fill="none" stroke="var(--teal)" stroke-width="3"/></svg>Invoicing through Supplier<br>Nook and Halvex Systems</div>
  </section>

  <p class="social-proof"><strong>Already trusted by BVH communities.</strong><br>Ask your peers at The Wendlow and The Fennick on Garrow.</p>

  <footer class="cta-band">
    <p class="cta-text">Book a <em>Free Walkthrough</em><br>of Your Community</p>
    <p class="cta-phone"><svg width="24" height="24" viewBox="0 0 24 24"><path d="M6 2 l4 5 l-2 3 a12 12 0 0 0 6 6 l3 -2 l5 4 l-2 4 c-10 0 -18 -8 -18 -18 Z" fill="var(--teal-light)"/></svg>512-555-0147</p>
    <p class="cta-email"><svg width="22" height="16" viewBox="0 0 22 16"><rect width="22" height="16" rx="2" fill="var(--teal-light)"/><path d="M1 2 l10 7 l10 -7" fill="none" stroke="var(--forest)" stroke-width="2"/></svg>support@quillonclean-example.com</p>
  </footer>

</main>
</div>
</body>
</html>
```